Retail pricing firm advising supermarkets needs a new sales brochure

We need a re-formatted version of our two-page sell sheet that is "sleek" and professional looking. Feel free to recreate the graphic on the first page.

Target Market(s)

Supermarket executives

Industry/Entity Type

Business services; consulting

Requirements
Nice to have
• Colors - My logo is a shade of blue and a shade of green. These primary colors may work well on the sell sheet. But I'm flexible about colors. Also, it's alright to recraft the graphic on the first page.

```html
<!DOCTYPE html>
<html lang="en">
<head>
<meta charset="utf-8">
<title>Shelfwise Pricing – Sell Sheet</title>
<link href="https://fonts.googleapis.com/css2?family=Poppins:ital,wght@0,400;0,500;0,600;0,700;1,500;1,600&family=Open+Sans:wght@400;600&display=swap" rel="stylesheet">
<style>
  :root{
    --bg:#e2e2e2;
    --paper:#ffffff;
    --blue:#1f6f9a;
    --navy:#1f4f7a;
    --teal:#2f9a8e;
    --teal-dark:#23877c;
    --sky:#3aa0c0;
    --green:#8cba3f;
    --grey:#8a8a8a;
    --ink:#2b2f36;
  }
  *{box-sizing:border-box;margin:0;padding:0}
  html,body{width:1200px;height:960px;overflow:hidden}
  body{background:var(--bg);font-family:"Poppins",sans-serif;color:var(--ink);position:relative}

  .page{position:absolute;top:195px;width:440px;height:570px;background:var(--paper);
        box-shadow:0 10px 30px rgba(0,0,0,.12);overflow:hidden}
  .page--front{left:140px}
  .page--back{left:620px}

  /* front */
  .brand{position:absolute;left:28px;top:22px;display:flex;align-items:center;gap:8px}
  .brand__mark{width:18px;height:18px;background:var(--green)}
  .brand__name{font-size:14px;font-weight:600;color:var(--blue);letter-spacing:.5px;text-transform:uppercase}
  .front__title{position:absolute;left:28px;top:58px;width:400px;font-size:16px;line-height:1.2;
        font-weight:700;color:var(--blue);text-transform:uppercase}
  .front__lede{position:absolute;left:28px;top:122px;width:384px;font-size:9.5px;line-height:1.4;
        font-weight:600;font-style:italic;color:var(--grey)}
  .wheel{position:absolute;left:110px;top:164px;width:220px;height:220px}
  .wheel text{font-family:"Poppins",sans-serif;fill:#fff;text-anchor:middle}
  .front__note{position:absolute;left:40px;top:394px;width:360px;text-align:center;font-size:9.5px;
        line-height:1.4;color:var(--grey)}
  .why__title{position:absolute;left:28px;top:438px;font-size:15px;line-height:1.2;font-weight:700;color:var(--teal);
        text-transform:uppercase;padding-bottom:2px;border-bottom:1.5px solid var(--teal)}
  .why__list{position:absolute;left:28px;top:472px;width:384px;display:flex;gap:10px}
  .feature{flex:1;display:flex;gap:5px;align-items:flex-start}
  .feature svg{flex:0 0 20px}
  .feature h3{font-size:7px;font-weight:700;color:var(--ink);line-height:1.2}
  .feature p{font-size:5.5px;line-height:1.35;color:var(--grey)}
  .contact{position:absolute;left:0;bottom:0;width:100%;height:56px;
        background:linear-gradient(90deg,var(--teal-dark),var(--teal));color:#fff;
        display:flex;justify-content:space-between;align-items:center;padding:0 28px}
  .contact__name{font-size:11px;font-weight:600;line-height:1.2;text-transform:uppercase}
  .contact__lines{font-family:"Open Sans",sans-serif;font-size:9px;line-height:1.5;text-align:left}

  /* back */
  .hero{position:absolute;left:0;top:0;width:100%;height:230px;
        background:linear-gradient(160deg,#3b3f44 0%,#6c6a5e 35%,#8f5a3e 55%,#5e7a4a 75%,#d7d3cb 100%)}
  .banner{position:absolute;left:0;top:218px;width:100%;height:112px;background:var(--teal);
        color:#fff;padding:18px 26px}
  .banner h2{font-size:18px;line-height:1.2;font-weight:700;text-transform:uppercase}
  .banner p{margin-top:8px;font-size:10px;line-height:1.4;font-weight:500}
  .section-title{font-size:15px;line-height:1.2;font-weight:700;color:var(--teal);text-transform:uppercase;
        display:inline-block;padding-bottom:2px;border-bottom:1.5px solid var(--teal)}
  .process{position:absolute;left:26px;top:346px;width:388px}
  .process__steps{display:flex;gap:30px;margin-top:12px}
  .step{flex:1;display:flex;flex-direction:column;align-items:center;text-align:center}
  .step h3{margin-top:6px;font-size:9px;font-weight:700}
  .step p{font-size:8px;font-style:italic;color:#555;line-height:1.3}
  .clients{position:absolute;left:26px;top:462px;width:388px}
  .clients__lede{font-size:8px;color:#555;margin-top:4px}
  .clients__grid{display:flex;flex-wrap:wrap;gap:6px 18px;margin-top:10px}
  .clients__grid span{font-size:10px;font-weight:700;color:var(--teal-dark)}
  .clients__more{margin-top:6px;font-size:8px;font-weight:600;color:var(--ink)}
</style>
</head>
<body>

<section class="page page--front">
  <div class="brand"><span class="brand__mark"></span><span class="brand__name">Shelfwise Pricing</span></div>
  <h1 class="front__title">Providing<br>supermarkets with state-of-the-art<br>retail pricing support</h1>
  <p class="front__lede">We help supermarket retailers manage prices effectively and strengthen their price-value image using proven pricing strategies and analytics.</p>

  <svg class="wheel" viewBox="0 0 260 260" aria-label="Six dimensions of price-value image">
    <g stroke="#fff" stroke-width="3">
      <path d="M130 10 A120 120 0 0 1 233.9 70 L180.2 101 A58 58 0 0 0 130 72Z" fill="#3a9d9a"/>
      <path d="M233.9 70 A120 120 0 0 1 233.9 190 L180.2 159 A58 58 0 0 0 180.2 101Z" fill="#3aa0c0"/>
      <path d="M233.9 190 A120 120 0 0 1 130 250 L130 188 A58 58 0 0 0 180.2 159Z" fill="#1f5b8a"/>
      <path d="M130 250 A120 120 0 0 1 26.1 190 L79.8 159 A58 58 0 0 0 130 188Z" fill="#aacb5e"/>
      <path d="M26.1 190 A120 120 0 0 1 26.1 70 L79.8 101 A58 58 0 0 0 79.8 159Z" fill="#9cc44a"/>
      <path d="M26.1 70 A120 120 0 0 1 130 10 L130 72 A58 58 0 0 0 79.8 101Z" fill="#8cba3f"/>
    </g>
    <circle cx="130" cy="130" r="54" fill="#fff" stroke="#e4e4e4" stroke-width="4"/>
    <text x="130" y="124" font-size="22" font-weight="700" style="fill:#555">6</text>
    <text x="130" y="139" font-size="8.5" font-weight="600" style="fill:#444">DIMENSIONS</text>
    <text x="130" y="149" font-size="5.5" style="fill:#888">of Price-Value Image</text>
    <g font-size="8" font-weight="500">
      <text x="175" y="52">Everyday</text><text x="175" y="62">Base Price</text>
      <text x="218" y="128">KEY VALUE</text><text x="218" y="138">ITEM</text>
      <text x="178" y="206">PROMOTIONAL</text><text x="178" y="216">PRICING</text>
      <text x="88" y="218">MERCHANDISING</text>
      <text x="44" y="128">VALUE</text><text x="44" y="138">ASSORTMENT</text>
      <text x="86" y="52">Price</text><text x="86" y="62">Communication</text>
    </g>
  </svg>

  <p class="front__note">Our proprietary methods, analytics, and decision-support tools have helped 60+ supermarket companies across North America grow profitably.</p>

  <h2 class="why__title">Why choose us?</h2>
  <div class="why__list">
    <div class="feature">
      <svg width="20" height="20" viewBox="0 0 20 20"><circle cx="10" cy="10" r="6" fill="none" stroke="#2b2f36" stroke-width="4" stroke-dasharray="3 2"/><circle cx="10" cy="10" r="2.5" fill="#2b2f36"/></svg>
      <div><h3>Custom Pricing Strategies</h3><p>Tailored to each supermarket for optimal pricing performance</p></div>
    </div>
    <div class="feature">
      <svg width="20" height="20" viewBox="0 0 20 20" fill="#1f6f9a"><rect x="2" y="13" width="3" height="6"/><rect x="7" y="10" width="3" height="9"/><rect x="12" y="12" width="3" height="7"/><path d="M2 9 L8 5 L12 8 L18 2" stroke="#1f6f9a" stroke-width="1.6" fill="none"/></svg>
      <div><h3>Data-Driven Insights</h3><p>Leverage analytics to strengthen your price-value image</p></div>
    </div>
    <div class="feature">
      <svg width="20" height="20" viewBox="0 0 20 20"><path d="M6 12 L4 19 L8 17 L10 19 L10 13Z M14 12 L16 19 L12 17 L10 19 L10 13Z" fill="#8cba3f"/><circle cx="10" cy="8" r="6" fill="#8cba3f"/><circle cx="10" cy="8" r="3" fill="#fff"/></svg>
      <div><h3>Proven Success</h3><p>Helping 60+ supermarkets grow profitably across North America.</p></div>
    </div>
  </div>

  <footer class="contact">
    <div class="contact__name">Contact<br>Dana Whitfield</div>
    <div class="contact__lines">Phone: 555-014-2298<br>Email: dana.whitfield@shelfwisepricing.com</div>
  </footer>
</section>

<section class="page page--back">
  <div class="hero" role="img" aria-label="Photo of a brightly lit supermarket aisle with stocked shelves and fresh produce"></div>
  <div class="banner">
    <h2>Unlock the full potential<br>of your pricing strategy</h2>
    <p>We help retailers optimize their pricing strategy through tailored solutions, advanced analytics, and proven decision-support tools that drive market success.</p>
  </div>

  <div class="process">
    <h2 class="section-title">Our 3-phase process</h2>
    <div class="process__steps">
      <div class="step">
        <svg width="30" height="30" viewBox="0 0 30 30" fill="#2b2f36"><rect x="4" y="18" width="5" height="10"/><rect x="12" y="12" width="5" height="16"/><rect x="20" y="4" width="5" height="24"/></svg>
        <h3>Strategy Development</h3><p>Develop a market-aligned pricing plan.</p>
      </div>
      <div class="step">
        <svg width="30" height="30" viewBox="0 0 30 30" fill="none" stroke="#2b2f36" stroke-width="3.5"><path d="M7 13 A9 9 0 0 1 23 10"/><path d="M23 17 A9 9 0 0 1 7 20"/><path d="M19 6 L24 10 L19 13" stroke-width="2.5"/><path d="M11 24 L6 20 L11 17" stroke-width="2.5"/></svg>
        <h3>Implementation &amp; Evaluation</h3><p>Adjust, optimize &amp; review quarterly for success.</p>
      </div>
    </div>
  </div>

  <div class="clients">
    <h2 class="section-title">Who we work with</h2>
    <p class="clients__lede">25+ years of success with 60+ North American supermarkets.</p>
    <div class="clients__grid">
      <span>Hollow Creek Farms</span><span>Allied Grocers</span><span>Cartwell</span>
      <span>Greenway</span><span>Mapleton Market</span><span>Brookers</span>
    </div>
    <p class="clients__more">And More ......</p>
  </div>
</section>

</body>
</html>
```